Business Card Design for a Personal Trainer

I need a business card design for my job as a personal trainer. It should have a unique, modern and exclusive design. On the front there should be only my logo with my name and my job. 0163/2918374 Tobias Kellinger Lindenfeldweg 14 80412 Munich Germany The most important contact information is the web adress. it can be bigger than the rest, but its not necessary. The card should be 8,5cmx5,5cm big. Font: Roboto. Colors: black, white, gray, 56c1ff.

```html
<!DOCTYPE html>
<html lang="de">
<head>
<meta charset="utf-8">
<title>Tobias Kellinger – Personal Trainer Visitenkarte</title>
<link href="https://fonts.googleapis.com/css2?family=Roboto:wght@300;400;500&display=swap" rel="stylesheet">
<style>
  :root {
    --page-bg: #eeeeee;
    --card-bg: #1d1d1d;
    --card-bg-deep: #161616;
    --text-light: #e6e6e6;
    --text-gray: #b3b3b3;
    --rule-gray: #8a8a8a;
    --accent: #56c1ff;
  }
  * { box-sizing: border-box; margin: 0; padding: 0; }
  html, body {
    width: 1200px; height: 1059px; overflow: hidden;
    background: var(--page-bg);
    font-family: "Roboto", Arial, sans-serif;
  }
  .stage {
    position: relative; width: 1200px; height: 1059px;
  }
  .card {
    position: absolute; left: 240px;
    width: 720px; height: 466px;
    background: radial-gradient(ellipse at 50% 40%, var(--card-bg) 0%, var(--card-bg-deep) 100%);
    box-shadow: 0 10px 24px rgba(0,0,0,.25);
    overflow: hidden;
  }
  .card--front { top: 40px; }
  .card--back { top: 553px; }

  /* Front */
  .brand {
    position: absolute; left: 0; right: 0; top: 178px;
    text-align: center; color: var(--text-gray);
  }
  .brand__name {
    display: inline-flex; align-items: center; gap: 14px;
    font-weight: 400; font-size: 34px; letter-spacing: 3px;
  }
  .brand__mark {
    width: 16px; height: 16px; background: var(--text-gray);
  }
  .brand__role {
    margin-top: 10px;
    display: flex; align-items: center; justify-content: center; gap: 12px;
    font-size: 13px; letter-spacing: 4px; font-weight: 400;
  }
  .brand__rule { width: 110px; height: 1px; background: var(--rule-gray); }

  /* Back */
  .portrait {
    position: absolute; left: 0; bottom: 0;
    width: 320px; height: 400px;
    background: linear-gradient(180deg, #3a3a3a 0%, #2b2b2b 55%, #1d1d1d 100%);
  }
  .back__name {
    position: absolute; left: 395px; top: 120px;
    color: var(--text-light); font-size: 30px; font-weight: 400; letter-spacing: .5px;
  }
  .contact {
    position: absolute; left: 355px; top: 330px;
    list-style: none; color: var(--text-light);
  }
  .contact__item {
    display: flex; align-items: center; gap: 14px;
    font-size: 15px; font-weight: 300; letter-spacing: .8px;
    height: 24px;
  }
  .contact__item--web { font-size: 20px; font-weight: 400; margin-top: 4px; height: 28px; }
  .contact__icon { width: 14px; height: 14px; fill: var(--text-gray); flex: none; }
</style>
</head>
<body>
<main class="stage">
  <section class="card card--front" aria-label="Vorderseite">
    <div class="brand">
      <div class="brand__name"><span class="brand__mark"></span>TOBIAS KELLINGER</div>
      <div class="brand__role"><span class="brand__rule"></span>PERSONAL TRAINER<span class="brand__rule"></span></div>
    </div>
  </section>

  <section class="card card--back" aria-label="Rückseite">
    <div class="portrait" role="img" aria-label="Schwarz-Weiß-Porträtfoto des Trainers mit verschränkten Armen"></div>
    <h1 class="back__name">Tobias Kellinger</h1>
    <ul class="contact">
      <li class="contact__item">
        <svg class="contact__icon" viewBox="0 0 14 14"><path d="M7 0a5 5 0 0 0-5 5c0 3.5 5 9 5 9s5-5.5 5-9a5 5 0 0 0-5-5zm0 7a2 2 0 1 1 0-4 2 2 0 0 1 0 4z"/></svg>
        Lindenfeldweg 14, München
      </li>
      <li class="contact__item">
        <svg class="contact__icon" viewBox="0 0 14 14"><path d="M3 1l2 0 1 3-1.5 1.2a8 8 0 0 0 4.3 4.3L10 8l3 1v2a2 2 0 0 1-2 2A11 11 0 0 1 1 3a2 2 0 0 1 2-2z"/></svg>
        0163/2918374
      </li>
      <li class="contact__item">
        <svg class="contact__icon" viewBox="0 0 14 14"><path d="M0 3h14v1L7 8 0 4zM0 5.5l7 4 7-4V11H0z"/></svg>
        t.kellinger@postfach.de
      </li>
      <li class="contact__item contact__item--web">
        <svg class="contact__icon" viewBox="0 0 14 14"><circle cx="7" cy="7" r="6.5"/><path d="M0.5 7h13M7 .5v13" stroke="#1d1d1d" stroke-width="1"/></svg>
        www.tobiaskellinger.de
      </li>
    </ul>
  </section>
</main>
</body>
</html>
```